Roll-up-Banner für Schule gesucht
Zielgruppe
Unsere Schule wünscht einen Rollup (880mm Breite x 2200mm Höhe) für die jährliche Lesenacht für Kinder im Alter von 6-12 Jahren. Diese wären die Produktdaten: https://blaetter.vimtral-laden.de/ro-04-85-roll-up-display-basic-85-produktblatt-productsheet.pdf
Der Rollup sollte für Kinder kreiert werden aber nicht zu kindlich sein.
Aufgabenstellung
Das Logo der Schule müsste ersichtlich sein ansonsten ist Kreativität gefragt ;-)

```html
<!DOCTYPE html>
<html lang="de">
<head>
<meta charset="utf-8">
<title>Roll-up Lesenacht – Schule Birkenau</title>
<link rel="stylesheet" href="https://fonts.googleapis.com/css2?family=Cormorant+Garamond:ital,wght@0,500;0,600;1,600&family=Fira+Sans:wght@500;600&display=swap">
<style>
  :root {
    --page-bg: #45484d;
    --banner-top: #dcdcdc;
    --banner-mid: #8a8a8a;
    --banner-low: #3e3e3e;
    --ink-light: #f1f0ee;
    --ink-dark: #262626;
    --school-green: #1f7a3a;
    --photo-warm: #8a6a3c;
    --photo-glow: #d9a94a;
    --photo-shade: #3a3226;
  }
  * { margin: 0; padding: 0; box-sizing: border-box; }
  html, body { width: 768px; height: 1200px; overflow: hidden; background: var(--page-bg); }
  .rollup {
    position: absolute; left: 139px; top: 0;
    width: 490px; height: 1200px;
    background: linear-gradient(180deg, var(--banner-top) 0%, #b9b9b9 25%, var(--banner-mid) 45%, var(--banner-low) 64%, #3a3a3a 100%);
    overflow: hidden;
  }
  .school-name {
    position: absolute; left: 0; right: 0; top: 150px;
    display: flex; align-items: center; justify-content: center; gap: 12px;
  }
  .school-name__dot { width: 14px; height: 14px; border-radius: 50%; background: var(--school-green); }
  .school-name__text {
    font-family: "Fira Sans", sans-serif; font-weight: 600;
    font-size: 25px; letter-spacing: 0.28em; color: var(--ink-dark);
  }
  .rule-top { position: absolute; left: 64px; top: 302px; width: 366px; height: 3px; background: var(--ink-light); }
  .quote {
    position: absolute; left: 0; right: 0; top: 350px;
    font-family: "Cormorant Garamond", serif; color: var(--ink-light);
    text-align: center; line-height: 1;
  }
  .quote__line1 { font-size: 56px; font-weight: 600; }
  .quote__line1 em { font-style: italic; }
  .quote__line2 { font-size: 100px; font-weight: 600; margin-top: -4px; }
  .quote__line3 { font-size: 64px; font-weight: 500; margin-top: -8px; }
  .rule-chevron { position: absolute; left: 64px; top: 650px; }
  .attribution {
    position: absolute; left: 0; right: 0; top: 724px;
    font-family: "Fira Sans", sans-serif; font-weight: 500; font-size: 17px;
    color: var(--ink-light); text-align: center;
  }
  .reading-photo {
    position: absolute; left: 0; right: 0; top: 760px; bottom: 0;
    background:
      radial-gradient(circle at 92% 78%, var(--photo-glow) 0%, rgba(217,169,74,0) 30%),
      radial-gradient(ellipse at 30% 55%, #c9b49a 0%, rgba(201,180,154,0) 55%),
      linear-gradient(180deg, rgba(62,62,62,1) 0%, var(--photo-warm) 45%, var(--photo-shade) 100%);
  }
</style>
</head>
<body>
  <main class="rollup">
    <div class="school-name">
      <span class="school-name__text">SCHULE BIRKENAU</span>
      <span class="school-name__dot"></span>
    </div>

    <div class="rule-top"></div>

    <h1 class="quote">
      <div class="quote__line1"><em>Lesen</em> ist ein</div>
      <div class="quote__line2">großes</div>
      <div class="quote__line3">Wunder.</div>
    </h1>

    <svg class="rule-chevron" width="366" height="48" viewBox="0 0 366 48" aria-hidden="true">
      <polyline points="0,2 146,2 183,44 220,2 366,2" fill="none" stroke="#f1f0ee" stroke-width="3"/>
    </svg>

    <p class="attribution">Klara von Eschenried-Hallbach</p>

    <div class="reading-photo" role="img" aria-label="Foto: Mädchen liest unter einer Decke ein Buch im Schein einer Laterne"></div>
  </main>
</body>
</html>
```